"Harborline Inc." Needs a Logo Design and Business Card

The name of the company is "Harborline Inc."
Our Business decription, which should appear on the front of the Business Card along with the logo and business name is:
"Boutique Global Procurement and Management Services"
We offer the following SERVICES that should be listed on the back of the Business Card :
"Consultants"
"Management"
"Business Research & Development"
"Sourcing Agent"
"Distributors"
We would like to see designs that use the colors
burnt orange and,
stainless steel
Business card designs should be innovatively modern and contemporary
Telephone number and email address should be on the back of the card
The name of the firm is "Harborline Inc.
Steel

```html
<!DOCTYPE html>
<html lang="en">
<head>
<meta charset="utf-8">
<title>Harborline Inc. – Logo and Business Card</title>
<link rel="stylesheet" href="https://fonts.googleapis.com/css2?family=Gochi+Hand&family=Arimo:wght@400;700&display=swap">
<style>
  :root {
    --ink: #000000;
    --paper: #ffffff;
    --burnt-orange: #c8551a;
    --steel: #8e979e;
    --steel-dark: #4f575d;
    --steel-light: #c9ced2;
    --card-tint: #eef0f2;
    --rule-steel: #9aa2a8;
    --script: "Gochi Hand", cursive;
    --sans: "Arimo", Arial, sans-serif;
  }
  html, body {
    margin: 0;
    padding: 0;
    width: 1200px;
    height: 948px;
    overflow: hidden;
    background: var(--paper);
  }
  .board {
    position: relative;
    width: 1200px;
    height: 948px;
    box-sizing: border-box;
    border: 1px solid var(--ink);
    font-family: var(--sans);
    color: var(--ink);
  }
  .logo-sheet {
    position: absolute;
    left: 332px; top: 27px;
    width: 536px; height: 440px;
    box-sizing: border-box;
    border: 1px solid var(--ink);
    background: var(--paper);
  }
  .card-sheet {
    position: absolute;
    left: 21px; top: 479px;
    width: 1146px; height: 439px;
    box-sizing: border-box;
    border: 1px solid var(--ink);
  }
  .side-label {
    position: absolute;
    top: 26px;
    width: 300px;
    margin-left: -150px;
    text-align: center;
    font-family: var(--sans);
    font-size: 44px;
    line-height: 1;
  }
  .side-label--front { left: 267px; }
  .side-label--back { left: 807px; }

  .card {
    position: absolute;
    top: 90px;
    width: 535px; height: 314px;
    box-sizing: border-box;
    background: var(--card-tint);
  }
  .card--front { left: 34px; border: 1px dashed #555; }
  .card--back { left: 577px; border: 1px solid var(--ink); }

  .artwork {
    position: absolute;
    border-radius: 48% 52% 40% 60% / 55% 50% 50% 45%;
    background: linear-gradient(160deg, var(--burnt-orange) 0%, var(--burnt-orange) 45%, var(--steel-dark) 62%, var(--steel-light) 100%);
  }
  .logo-sheet .artwork { left: 180px; top: 34px; width: 240px; height: 262px; }
  .card--front .artwork { left: 200px; top: 36px; width: 150px; height: 148px; }

  .brand-name {
    position: absolute;
    left: 0; right: 0;
    text-align: center;
    font-family: var(--script);
    font-weight: 400;
    color: var(--burnt-orange);
    line-height: 1;
    margin: 0;
  }
  .logo-sheet .brand-name { top: 274px; font-size: 74px; }
  .card--front .brand-name { top: 176px; font-size: 46px; }

  .tagline {
    position: absolute;
    left: 0; right: 0;
    text-align: center;
    font-family: var(--sans);
    font-weight: 700;
    margin: 0;
    line-height: 1;
  }
  .logo-sheet .tagline { top: 349px; font-size: 16.5px; left: 30px; }
  .card--front .tagline { top: 228px; font-size: 10.2px; }

  .card-rules {
    position: absolute;
    left: 0; top: 0;
    width: 535px; height: 314px;
  }
  .service-list {
    list-style: none;
    margin: 0; padding: 0;
  }
  .service-list li,
  .contact-line {
    position: absolute;
    font-family: var(--script);
    font-size: 18px;
    line-height: 1;
    white-space: nowrap;
  }
  .service-list li { left: 55px; }
  .contact-line { right: 31px; text-align: right; margin: 0; }
</style>
</head>
<body>
<main class="board">

  <section class="logo-sheet" aria-label="Logo">
    <div class="artwork" role="img" aria-label="Brand illustration area in burnt orange and stainless steel tones"></div>
    <h1 class="brand-name">Harborline Inc.</h1>
    <p class="tagline">Boutique Global Procurement and Management Services</p>
  </section>

  <section class="card-sheet" aria-label="Business card">
    <div class="side-label side-label--front">Front</div>
    <div class="side-label side-label--back">Back</div>

    <article class="card card--front">
      <div class="artwork" role="img" aria-label="Brand illustration area in burnt orange and stainless steel tones"></div>
      <h2 class="brand-name">Harborline Inc.</h2>
      <p class="tagline">Boutique Global Procurement and Management Services</p>
    </article>

    <article class="card card--back">
      <svg class="card-rules" viewBox="0 0 535 314" aria-hidden="true">
        <g stroke="var(--rule-steel)" stroke-width="1.5">
          <line x1="0" y1="71" x2="322" y2="71"/>
          <line x1="0" y1="112" x2="322" y2="112"/>
          <line x1="0" y1="147" x2="322" y2="147"/>
          <line x1="0" y1="184" x2="322" y2="184"/>
          <line x1="329" y1="262" x2="535" y2="262"/>
        </g>
        <g fill="var(--burnt-orange)">
          <circle cx="322" cy="71" r="3.5"/>
          <circle cx="322" cy="112" r="3.5"/>
          <circle cx="322" cy="147" r="3.5"/>
          <circle cx="322" cy="184" r="3.5"/>
          <circle cx="329" cy="262" r="3.5"/>
        </g>
      </svg>
      <ul class="service-list">
        <li style="top:45px">Consultants</li>
        <li style="top:81px">Management</li>
        <li style="top:117px">Business Research &amp; Development</li>
        <li style="top:154px">Sourcing Agent</li>
        <li style="top:190px">Distributors</li>
      </ul>
      <p class="contact-line" style="top:236px">Telephone number</p>
      <p class="contact-line" style="top:266px">email address</p>
    </article>
  </section>

</main>
</body>
</html>
```